Business card design Needed for new logo / Construction business, home extensions and new builds

We need a business card design using our new logo files which i will attach to this project :)

We are a small construction business specialising in home extensions, new builds and property development. We are very ambitious and would appreciate professional and elegant designs for our new business card.

Very serious about using the services on Sketchwharf and recently acquired our new logo from here :)

Please get involved, i will feedback when i can as i am very busy but can respond daily, thanks

Target Market(s)

People that want to build onto their houses, new building developments or adding too their existing property

Industry/Entity Type

Construction

Contact Information for Business Card

Thornley Pike Construction, Wilbur Fenwick (Managing Director), Tel 07829456172, email - info@thornley-pike, www.thornley-pike.co.uk

Colors

Designer to choose colors to be used in the design.

Requirements
Must have
• I like a deep grey on the back please. A lot of you have provided black from and back, try mixing things up a little. The black looks cool 😎 Thanks

```html
<!DOCTYPE html>
<html lang="en">
<head>
<meta charset="utf-8">
<title>Thornley Pike Construction – Business Card</title>
<link href="https://fonts.googleapis.com/css2?family=Open+Sans:wght@400;600;700;800&display=swap" rel="stylesheet">
<style>
  :root {
    --stage: #222222;
    --card-black: #1f1f22;
    --card-grey: #8e959b;
    --grey-light: #a5abb0;
    --grey-dark: #6f767c;
    --gold-light: #f3c75a;
    --gold: #d9a431;
    --gold-dark: #9c6d14;
    --silver-light: #f2f3f4;
    --silver: #c3c6c9;
    --silver-dark: #7f8488;
    --white: #ffffff;
  }
  * { margin: 0; padding: 0; box-sizing: border-box; }
  html, body { width: 1200px; height: 780px; overflow: hidden; }
  body {
    background: var(--stage);
    font-family: "Open Sans", Arial, sans-serif;
    position: relative;
  }
  .card {
    position: absolute;
    width: 540px;
    height: 310px;
    border-radius: 18px;
    overflow: hidden;
    box-shadow: 0 14px 30px rgba(0,0,0,.55);
  }

  /* Back */
  .card-back { left: 70px; top: 70px; background: var(--card-grey); }
  .back-pattern {
    position: absolute; inset: 0;
    background: linear-gradient(160deg, var(--grey-light) 0%, var(--card-grey) 50%, var(--grey-dark) 100%);
  }
  .back-wordmark {
    position: absolute; right: 26px; bottom: 92px;
    display: flex; align-items: center; gap: 6px;
    font-size: 8px; font-weight: 600; color: var(--white);
    letter-spacing: .5px; text-transform: uppercase;
  }
  .back-wordmark .mark-square { width: 10px; height: 10px; background: var(--white); }

  /* Front */
  .card-front { left: 590px; top: 400px; background: var(--card-black); }
  .brand {
    position: absolute; left: 30px; top: 110px; width: 210px;
    display: flex; flex-direction: column; align-items: center; gap: 10px;
  }
  .brand .mark-square { width: 34px; height: 34px; background: var(--gold); }
  .brand-name {
    font-size: 17px; font-weight: 600; color: var(--silver);
    text-transform: uppercase; letter-spacing: 1px; text-align: center; line-height: 1.3;
  }
  .divider {
    position: absolute; left: 262px; top: 50px; width: 1px; height: 170px;
    background: linear-gradient(var(--silver-dark), var(--white), var(--silver-dark));
  }
  .contact { position: absolute; left: 284px; top: 52px; color: var(--white); }
  .person-name { font-size: 25px; font-weight: 800; line-height: 1.1; }
  .person-first { color: var(--silver); }
  .person-last { color: var(--gold); }
  .person-role { font-size: 12px; font-weight: 600; margin-top: 3px; }
  .contact-list { list-style: none; margin-top: 30px; font-size: 12.5px; }
  .contact-list li { display: flex; align-items: center; gap: 9px; margin-bottom: 5px; }
  .contact-list svg { width: 12px; height: 12px; flex: none; }
  .address {
    position: absolute; left: 0; right: 0; bottom: 48px;
    text-align: center; font-size: 13px; color: var(--white); letter-spacing: .3px;
  }
  .band { position: absolute; bottom: 0; height: 26px; }
  .band-gold {
    left: 0; width: 58%;
    background: linear-gradient(var(--gold-light), var(--gold) 50%, var(--gold-dark));
    clip-path: polygon(0 0, 100% 0, 93% 100%, 0 100%);
  }
  .band-silver {
    right: 0; width: 46%;
    background: linear-gradient(var(--silver-light), var(--silver) 50%, var(--silver-dark));
    clip-path: polygon(8% 0, 100% 0, 100% 100%, 0 100%);
  }
</style>
</head>
<body>
  <section class="card card-back">
    <div class="back-pattern" role="img" aria-label="Repeating tonal monogram pattern in light and dark grey"></div>
    <div class="back-wordmark"><span class="mark-square"></span>Thornley Pike Construction</div>
  </section>

  <section class="card card-front">
    <div class="brand">
      <span class="mark-square"></span>
      <div class="brand-name">Thornley Pike<br>Construction</div>
    </div>

    <div class="divider"></div>

    <div class="contact">
      <h1 class="person-name"><span class="person-first">Wilbur</span> <span class="person-last">Fenwick</span></h1>
      <p class="person-role">Managing Director</p>
      <ul class="contact-list">
        <li>
          <svg viewBox="0 0 24 24" fill="var(--gold)"><path d="M6.6 10.8a15 15 0 0 0 6.6 6.6l2.2-2.2c.3-.3.7-.4 1-.2 1.1.4 2.3.6 3.6.6.6 0 1 .4 1 1V20c0 .6-.4 1-1 1A17 17 0 0 1 3 4c0-.6.4-1 1-1h3.5c.6 0 1 .4 1 1 0 1.3.2 2.5.6 3.6.1.3 0 .7-.2 1z"/></svg>
          0782 945 6172
        </li>
        <li>
          <svg viewBox="0 0 24 24" fill="none" stroke="var(--gold)" stroke-width="2"><circle cx="12" cy="12" r="9"/><path d="M3 12h18M12 3c3 3 3 15 0 18M12 3c-3 3-3 15 0 18"/></svg>
          info@thornley-pike.co.uk
        </li>
        <li>
          <svg viewBox="0 0 24 24" fill="none" stroke="var(--gold)" stroke-width="2"><rect x="3" y="6" width="18" height="13" rx="1"/><path d="M3 7l9 7 9-7"/></svg>
          www.thornley-pike.co.uk
        </li>
      </ul>
    </div>

    <p class="address">Ashcombe Lane, Westbourne Poole, BH4 7QT</p>

    <div class="band band-gold"></div>
    <div class="band band-silver"></div>
  </section>
</body>
</html>
```